Looking for a dynamic business card for a pizzeria.

A business card with our food, logo, and space for name, title, email, website, phone. The card should convey quality, unique, amazing. On the front, I envision food photo or photos with the owners names and contact information. On the back, more food with locations, website, facebook, twitter, instagram icons. It should look polished, not cartoonish, or plain.
Target Market(s)
upscale, local food buyers, 30-50 years in age.
Industry/Entity Type
Restaurant
Contact Information for Business Card
Business Name: Crustelli, LLC
Website: www.crustelli-example.com
Back:
2 locations: (can list on the back of card)
1. Marlow Point
3807 Marlow Street
Cedarvale, WA 98002
360-555-0143
2. Quenby Heights
1736 Quenby Street
Cedarvale, WA 98001
360-555-0187
front:
EDITABLE space for
Business name
Person's Name
title
2nd title
Email address
cell-phone number
Requirements
Must have
- logo
- my food photo or photos (no watermarks showing)
- locations on back
- Person contact information on front
- full bleed

```html
<!DOCTYPE html>
<html lang="en">
<head>
<meta charset="utf-8">
<title>Crustelli Business Card</title>
<link rel="stylesheet" href="https://fonts.googleapis.com/css2?family=Didact+Gothic&display=swap">
<style>
  :root {
    --bg: #e9e6e1;
    --card: #ffffff;
    --green: #2f6b3a;
    --red: #c0161b;
    --ink: #2b2b2b;
    --dough-light: #e8e2da;
    --dough-mid: #b9aea3;
    --dough-dark: #6e655d;
  }
  * { box-sizing: border-box; margin: 0; padding: 0; }
  html, body { width: 1200px; height: 843px; overflow: hidden; }
  body {
    background: var(--bg);
    font-family: "Didact Gothic", sans-serif;
    position: relative;
  }
  .card {
    position: absolute;
    width: 540px;
    height: 309px;
    background: var(--card);
    overflow: hidden;
    box-shadow: 0 6px 18px rgba(0,0,0,0.18);
  }
  .card--back { left: 40px; top: 267px; }
  .card--front { left: 620px; top: 267px; }

  /* back */
  .back-photo {
    position: absolute; right: 0; top: 0; width: 290px; height: 100%;
    background: linear-gradient(120deg, var(--dough-light) 0%, var(--dough-mid) 55%, var(--dough-dark) 100%);
  }
  .back-info { position: absolute; left: 26px; top: 34px; width: 215px; }
  .wordmark {
    display: flex; align-items: center; gap: 8px;
    color: var(--green); font-size: 34px; letter-spacing: 1px; line-height: 1;
    white-space: nowrap;
  }
  .back-info .wordmark { font-size: 28px; }
  .wordmark__dot { width: 20px; height: 20px; border-radius: 50%; background: var(--red); flex: none; }
  .location { margin-top: 22px; font-size: 14px; line-height: 1.3; color: var(--ink); white-space: nowrap; }
  .location + .location { margin-top: 14px; }
  .location__name, .location__label { color: var(--green); }

  /* front */
  .front-shape { position: absolute; inset: 0; width: 100%; height: 100%; }
  .front-info { position: absolute; left: 30px; top: 26px; }
  .front-info .wordmark { font-size: 38px; }
  .person { margin-top: 14px; color: var(--green); font-size: 22px; letter-spacing: 1px; }
  .person__title { color: var(--red); font-size: 16px; margin-top: 2px; }
  .contacts { list-style: none; margin-top: 16px; font-size: 15px; color: var(--ink); }
  .contacts li { display: flex; align-items: center; gap: 10px; line-height: 1.6; }
  .contacts svg { width: 14px; height: 14px; fill: var(--green); flex: none; }
  .social { position: absolute; right: 22px; bottom: 22px; display: flex; gap: 10px; }
  .social span { width: 18px; height: 18px; border-radius: 50%; background: var(--card); opacity: 0.9; }
</style>
</head>
<body>
  <section class="card card--back">
    <div class="back-info">
      <div class="wordmark"><span>CRUSTELLI</span><span class="wordmark__dot"></span></div>
      <p class="location">
        <span class="location__name">Quenby Heights</span><br>
        1736 Quenby Street<br>
        Cedarvale, WA 98001<br>
        <span class="location__label">Phone:</span>360-555-0187
      </p>
      <p class="location">
        <span class="location__name">Marlow Point</span><br>
        3807 Marlow Street<br>
        Cedarvale, WA 98002<br>
        <span class="location__label">Phone:</span>360-555-0143
      </p>
    </div>
    <div class="back-photo" role="img" aria-label="Photo of a chef's hands shaping pizza dough with a dusting of flour"></div>
  </section>

  <section class="card card--front">
    <svg class="front-shape" viewBox="0 0 540 309" preserveAspectRatio="none" aria-hidden="true">
      <rect width="540" height="309" fill="var(--red)"/>
      <path d="M0 0 H300 C400 40 470 120 470 190 C470 230 440 250 400 255 C300 240 150 225 0 262 Z" fill="var(--card)"/>
    </svg>
    <div class="front-info">
      <div class="wordmark"><span>CRUSTELLI</span></div>
      <p class="person">MARCO BELLINI</p>
      <p class="person__title">Founder</p>
      <ul class="contacts">
        <li><svg viewBox="0 0 14 14"><path d="M4 0h6a1 1 0 0 1 1 1v12a1 1 0 0 1-1 1H4a1 1 0 0 1-1-1V1a1 1 0 0 1 1-1zm0 2v9h6V2z"/></svg>689 555 0162</li>
        <li><svg viewBox="0 0 14 14"><path d="M0 3h14v8H0zM1 4l6 4 6-4v-0.5H1z" fill-rule="evenodd"/></svg>name@crustelli-example.com</li>
        <li><svg viewBox="0 0 14 14"><circle cx="7" cy="7" r="6"/></svg>www.crustelli-example.com</li>
      </ul>
    </div>
    <div class="social" aria-hidden="true"><span></span><span></span><span></span></div>
  </section>
</body>
</html>
```